Release Therapy business card that deals with the release of negative issues

I need a business card for my business called PEBBLES (A warm hearth to rest when you tire) ... I'm a therapist that deals with people releasing negative issues, by applying therapies that incorporate, hypnosis, aromatherapy and listen therapy..I like the colour green and soft blues...My idea is for a hand releasing butterflies, and incorporating soft clouds....
Target Market(s)
All people, all ages
Industry/Entity Type
Business
Contact Information for Business Card
PEBBLES"A Warm Hearth To Rest When You Tire"Yvette R BrockingtonRelease Therapist0411 743 781email: calmingpaths4you@quietmail.example
Requirements
Must have
- butterflies and soft clouds
Nice to have
- I like the decorative and script fonts for business name, and also my name
- Marisol T Fenwhistle...

```html
<!DOCTYPE html>
<html lang="en">
<head>
<meta charset="utf-8">
<title>Pebbles – Release Therapist Business Card</title>
<link rel="stylesheet" href="https://fonts.googleapis.com/css2?family=Allura&family=Lato:wght@400&family=Questrial&display=swap">
<style>
  :root {
    --canvas-bg: #ebebe8;
    --card-white: #ffffff;
    --sky-top: #8cc6ee;
    --sky-bottom: #d9eefb;
    --cloud-white: #f7fbfe;
    --green-bright: #3db54a;
    --green-mid: #2a9e40;
    --green-deep: #1b7f33;
    --green-script: #2fae48;
    --ink: #333a3d;
    --ink-soft: #4a5256;
    --butterfly-teal: #2a9fa8;
    --butterfly-dark: #1d5e6a;
    --skin: #f1c9ad;
  }
  * { box-sizing: border-box; margin: 0; padding: 0; }
  html, body {
    width: 1200px;
    height: 788px;
    overflow: hidden;
    background: var(--canvas-bg);
  }
  .canvas {
    width: 1200px;
    height: 788px;
    display: flex;
    align-items: center;
    justify-content: center;
    gap: 50px;
  }
  .card {
    position: relative;
    width: 540px;
    height: 330px;
    overflow: hidden;
    border-radius: 4px;
    box-shadow: 0 6px 18px rgba(0,0,0,0.14);
  }
  .card__art {
    position: absolute;
    inset: 0;
    width: 100%;
    height: 100%;
  }

  /* Front side */
  .card--front { background: linear-gradient(180deg, var(--sky-top), var(--sky-bottom)); }
  .sky-clouds {
    position: absolute;
    left: 40px;
    top: 70px;
    width: 440px;
    height: 170px;
    border-radius: 50%;
    background: radial-gradient(ellipse at center, rgba(255,255,255,0.85), rgba(255,255,255,0) 70%);
  }
  .brand-name {
    position: absolute;
    left: 34px;
    top: 62px;
    font-family: "Allura", cursive;
    font-size: 104px;
    line-height: 1;
    color: var(--green-script);
  }
  .brand-tagline {
    position: absolute;
    left: 30px;
    top: 184px;
    font-family: "Lato", sans-serif;
    font-size: 19px;
    color: var(--ink);
  }
  .butterfly-flock {
    position: absolute;
    left: 300px;
    top: 50px;
    width: 170px;
    height: 150px;
    border-radius: 40%;
    background: radial-gradient(ellipse at 45% 55%, rgba(42,159,168,0.55), rgba(42,159,168,0) 70%);
  }
  .releasing-hand {
    position: absolute;
    left: 170px;
    top: 200px;
    width: 160px;
    height: 120px;
    border-radius: 60% 40% 30% 50%;
    background: radial-gradient(ellipse at 60% 35%, rgba(241,201,173,0.95), rgba(241,201,173,0) 72%);
  }

  /* Back side */
  .card--back { background: var(--card-white); }
  .contact {
    position: absolute;
    left: 150px;
    top: 58px;
    text-align: center;
    width: 250px;
  }
  .contact__name {
    font-family: "Allura", cursive;
    font-size: 34px;
    line-height: 1;
    color: var(--green-script);
  }
  .contact__role {
    font-family: "Questrial", sans-serif;
    font-size: 15px;
    letter-spacing: 1px;
    color: var(--ink);
    margin-top: 4px;
  }
  .contact__phone {
    font-family: "Questrial", sans-serif;
    font-size: 15px;
    letter-spacing: 3px;
    color: var(--ink-soft);
    margin-top: 20px;
  }
  .contact__email {
    font-family: "Questrial", sans-serif;
    font-size: 13px;
    letter-spacing: 0.5px;
    color: var(--ink-soft);
    margin-top: 8px;
    white-space: nowrap;
    margin-left: -60px;
    width: 370px;
  }
  .butterfly-single {
    position: absolute;
    right: 38px;
    top: 62px;
    width: 96px;
    height: 66px;
    border-radius: 50%;
    background: radial-gradient(ellipse at center, var(--butterfly-teal), rgba(42,159,168,0) 72%);
  }
</style>
</head>
<body>
<main class="canvas">

  <section class="card card--front" aria-label="Business card front">
    <div class="sky-clouds" role="img" aria-label="Soft white clouds in a blue sky"></div>
    <div class="butterfly-flock" role="img" aria-label="Teal butterflies rising into the sky"></div>
    <div class="releasing-hand" role="img" aria-label="Open hand releasing butterflies"></div>
    <svg class="card__art" viewBox="0 0 540 330" preserveAspectRatio="none" aria-hidden="true">
      <path d="M0,330 L0,296 C190,292 390,228 540,112 L540,330 Z" fill="var(--green-bright)"/>
      <path d="M0,302 C200,297 395,232 540,124 L540,150 C395,258 200,314 0,316 Z" fill="var(--green-deep)"/>
      <path d="M0,318 C200,316 400,262 540,160 L540,170 C400,272 200,324 0,325 Z" fill="var(--green-mid)"/>
    </svg>
    <h1 class="brand-name">Pebbles</h1>
    <p class="brand-tagline">A Warm Hearth To Rest When You Tire</p>
  </section>

  <section class="card card--back" aria-label="Business card back">
    <svg class="card__art" viewBox="0 0 540 330" preserveAspectRatio="none" aria-hidden="true">
      <path d="M0,330 L0,300 C200,300 400,270 540,222 L540,330 Z" fill="var(--green-bright)"/>
      <path d="M0,306 C200,306 400,276 540,228 L540,246 C400,294 200,318 0,318 Z" fill="var(--green-deep)"/>
    </svg>
    <div class="butterfly-single" role="img" aria-label="Teal butterfly"></div>
    <div class="contact">
      <p class="contact__name">Marisol T Fenwhistle</p>
      <p class="contact__role">Release Therapist</p>
      <p class="contact__phone">0482 516 904</p>
      <p class="contact__email">email: calmingpaths4you@quietmail.example</p>
    </div>
  </section>

</main>
</body>
</html>
```